Bref créative
Newspaper Ad for Immigration Law Firm
Need Three Ads/Sizes
I need a total of 3 newspaper ads with 3 different sizes.
1. Main Ad - 5 in x 2 in
2. 3.25 in x 2 in
3. 1.5 in x 2 in
Designers should submit their design based on the 5 in x 2 in. Once I have determined the "winning designer," I will work with that designer to create the other two ads using the same winning design.
Law
The following must be included: I will also upload my picture, my logo, and Board Certified Logo. Thanks.
1. Picture of Attorney
2. Attorney
3. Brian K. Wendell
4. Law Firm logo
5. Board Certified Logo
6. Immigration Law below Board Certified Logo
7. 4180 Millbrook Lane
8. Suite 318
9. Houston, Texas 77043
10. www.thewendellcounsel.com
11. Telephone: (713) 548-2190
12. Fax: (713) 548-2197
13. bkellan4471@mailvexo.com
14. Immigration Bonds
15. Deportation Cases
16. Immigration Court
17. Immigration Waivers
18. Immigration Appeals
19. Family Petitions
20. Citizenship
21. Permanent Residency
22. Asylum, TPS, NACARA
23. Work Permits
24. Other Immigration Cases
Law Firm Logo Should go on the very top i think
You can cut out background if you like. Or not, up to your design.
The phrase "Immigration Law" must be directly underneath this logo. Logo cannot be changed or altered.
Sample proof

```html
<!DOCTYPE html>
<html lang="en">
<head>
<meta charset="utf-8">
<title>Brian K. Wendell – 1.5 x 2 Newspaper Ad</title>
<link href="https://fonts.googleapis.com/css2?family=Cinzel:wght@500;700&family=Crimson+Text:wght@400;600&family=Roboto+Condensed:wght@700&display=swap" rel="stylesheet">
<style>
  :root {
    --board-center: #5b5b5b;
    --board-edge: #161616;
    --label: #cfcfcf;
    --caption: #8a8a8a;
    --paper: #ffffff;
    --ink: #1b2540;
    --ink-soft: #2c2c2c;
    --band-top: #4a1418;
    --band-bottom: #2a0a0c;
    --band-text: #ffffff;
    --badge: #1b2540;
    --mark: #1b2540;
  }
  * { box-sizing: border-box; margin: 0; padding: 0; }
  html, body { width: 1200px; height: 901px; overflow: hidden; }
  body {
    position: relative;
    background: radial-gradient(ellipse at 50% 45%, var(--board-center) 0%, #3a3a3a 45%, var(--board-edge) 100%);
    font-family: "Crimson Text", Georgia, serif;
  }
  .board-label {
    position: absolute; left: 17px; top: 18px;
    color: var(--label);
    font: 400 16px/1 "Roboto Condensed", Arial, sans-serif;
    letter-spacing: 0.5px;
  }
  .board-caption {
    position: absolute; left: 630px; top: 784px; width: 302px;
    text-align: center; color: var(--caption);
    font: 400 15px/1 "Roboto Condensed", Arial, sans-serif;
  }

  /* Ad component */
  .ad {
    position: absolute; width: 302px; height: 401px;
    background: var(--paper);
    box-shadow: 0 4px 14px rgba(0,0,0,.45);
  }
  .ad--color { left: 260px; top: 217px; }
  .ad--mono {
    left: 630px; top: 365px;
    --ink: #111111; --ink-soft: #1a1a1a;
    --band-top: #2b2b2b; --band-bottom: #0d0d0d;
    --badge: #222222; --mark: #222222;
  }

  .ad-header {
    height: 83px; display: flex; align-items: center; gap: 10px;
    padding: 0 10px 0 12px;
  }
  .firm-mark {
    flex: none; width: 60px; height: 60px; border-radius: 50%;
    background: var(--mark);
  }
  .firm-name {
    color: var(--ink); text-align: center; flex: 1;
    font-family: "Cinzel", Georgia, serif; font-weight: 500;
  }
  .firm-name .pre { font-size: 12px; letter-spacing: 1px; display: block; }
  .firm-name .main { font-size: 18px; line-height: 1.15; display: block; }
  .firm-name .post { font-size: 12px; letter-spacing: .5px; display: block; }

  .practice-band {
    height: 153px;
    background: linear-gradient(180deg, var(--band-top), var(--band-bottom));
    display: flex; padding: 16px 6px 0 10px;
    color: var(--band-text);
    font: 700 16px/26px "Roboto Condensed", Arial, sans-serif;
    letter-spacing: -0.2px;
  }
  .practice-list { list-style: none; }
  .practice-list--left { width: 150px; }
  .practice-list--right { flex: 1; }
  .practice-list li { padding-left: 10px; position: relative; }
  .practice-list li::before { content: "•"; position: absolute; left: 0; }
  .practice-list li.two-line { line-height: 16px; padding-top: 5px; padding-bottom: 5px; }

  .ad-footer { position: relative; height: 165px; padding: 0 8px; color: var(--ink-soft); }
  .attorney { position: absolute; left: 10px; top: 14px; color: var(--ink); }
  .attorney-name { font: 600 17px/1 "Cinzel", Georgia, serif; }
  .attorney-title { font: 600 11px/1 "Cinzel", Georgia, serif; letter-spacing: 1px; margin-top: 5px; text-align: center; }
  .certification { position: absolute; right: 12px; top: 8px; width: 110px; }
  .cert-badge { width: 110px; height: 34px; border-radius: 4px; background: var(--badge); }
  .cert-field { font: 400 10px/1 "Crimson Text", Georgia, serif; margin-top: 3px; color: var(--ink); }
  .contact {
    position: absolute; left: 0; right: 0; top: 62px; text-align: center;
    font-size: 11.5px; line-height: 15px;
  }
  .contact .row { display: flex; justify-content: space-around; }
  .phone {
    position: absolute; left: 0; right: 0; top: 96px; text-align: center;
    font: 400 37px/1 "Crimson Text", Georgia, serif; color: #111;
  }
  .website {
    position: absolute; left: 0; right: 0; top: 140px; text-align: center;
    font: 400 14px/1 "Crimson Text", Georgia, serif; letter-spacing: 1.6px; color: #111;
  }
</style>
</head>
<body>
  <div class="board-label">1.5” x 2” Newspaper Ad</div>

  <article class="ad ad--color">
    <header class="ad-header">
      <div class="firm-mark"></div>
      <div class="firm-name">
        <span class="pre">Law Office of</span>
        <span class="main">BRIAN K. WENDELL</span>
        <span class="post">Immigration Law Firm</span>
      </div>
    </header>
    <section class="practice-band">
      <ul class="practice-list practice-list--left">
        <li>Immigration Bonds</li>
        <li>Deportation Cases</li>
        <li>Immigration Court</li>
        <li>Immigration Waivers</li>
        <li>Immigration Appeals</li>
      </ul>
      <ul class="practice-list practice-list--right">
        <li>Family Petitions</li>
        <li>Citizenship</li>
        <li class="two-line">Permanent<br>Residency</li>
        <li class="two-line">Other Immigration<br>Cases</li>
      </ul>
    </section>
    <footer class="ad-footer">
      <div class="attorney">
        <div class="attorney-name">BRIAN K. WENDELL</div>
        <div class="attorney-title">ATTORNEY</div>
      </div>
      <div class="certification">
        <div class="cert-badge"></div>
        <div class="cert-field">Immigration Law</div>
      </div>
      <div class="contact">
        <div>4180 Millbrook Lane Suite 318 Houston, Texas 77043</div>
        <div class="row"><span>Fax: (713) 548-2197</span><span>Email: bkellan4471@mailvexo.com</span></div>
      </div>
      <div class="phone">(713) 548-2190</div>
      <div class="website">www.thewendellcounsel.com</div>
    </footer>
  </article>

  <article class="ad ad--mono">
    <header class="ad-header">
      <div class="firm-mark"></div>
      <div class="firm-name">
        <span class="pre">Law Office of</span>
        <span class="main">BRIAN K. WENDELL</span>
        <span class="post">Immigration Law Firm</span>
      </div>
    </header>
    <section class="practice-band">
      <ul class="practice-list practice-list--left">
        <li>Immigration Bonds</li>
        <li>Deportation Cases</li>
        <li>Immigration Court</li>
        <li>Immigration Waivers</li>
        <li>Immigration Appeals</li>
      </ul>
      <ul class="practice-list practice-list--right">
        <li>Family Petitions</li>
        <li>Citizenship</li>
        <li class="two-line">Permanent<br>Residency</li>
        <li class="two-line">Other Immigration<br>Cases</li>
      </ul>
    </section>
    <footer class="ad-footer">
      <div class="attorney">
        <div class="attorney-name">BRIAN K. WENDELL</div>
        <div class="attorney-title">ATTORNEY</div>
      </div>
      <div class="certification">
        <div class="cert-badge"></div>
        <div class="cert-field">Immigration Law</div>
      </div>
      <div class="contact">
        <div>4180 Millbrook Lane Suite 318 Houston, Texas 77043</div>
        <div class="row"><span>Fax: (713) 548-2197</span><span>Email: bkellan4471@mailvexo.com</span></div>
      </div>
      <div class="phone">(713) 548-2190</div>
      <div class="website">www.thewendellcounsel.com</div>
    </footer>
  </article>

  <div class="board-caption">Black &amp; White simulation</div>
</body>
</html>
```